Etiketten für Deodorant in fester Form
Zielgruppe
Naturkosmetik
Aufgabenstellung
Dimension of the tube:
The height of the tube’s body is 53mm
The height of the lid is 20mm
The circular of the body is 126mm

```html
<!DOCTYPE html>
<html lang="fr">
<head>
<meta charset="utf-8">
<title>Déodorant solide – étiquette</title>
<link href="https://fonts.googleapis.com/css2?family=Caveat+Brush&family=Montserrat:wght@400;600;700&family=Cairo:wght@600;700&display=swap" rel="stylesheet">
<style>
  :root{
    --bg:#f4f2ef;
    --cream:#fbf5dc;
    --orange:#e8502a;
    --coral:#f08a6a;
    --peach:#f7c9b3;
    --blush:#f9d9c8;
    --wine:#a8243a;
    --tan:#c98a6b;
    --teal:#6fc3bd;
    --ink:#3a3a3a;
  }
  html,body{margin:0;padding:0;width:759px;height:1200px;overflow:hidden;background:var(--bg);}
  body{font-family:"Montserrat",sans-serif;}
  .label{
    position:absolute;left:30px;top:454px;width:700px;height:292px;
    display:flex;box-shadow:0 3px 8px rgba(0,0,0,.18);overflow:hidden;
  }
  .decor{height:100%;}
  .decor--left{width:106px;background:
    radial-gradient(ellipse 70% 45% at 35% 52%,var(--orange) 0%,var(--orange) 55%,rgba(232,80,42,0) 75%),
    radial-gradient(ellipse 60% 30% at 45% 82%,var(--coral) 0%,rgba(240,138,106,0) 80%),
    var(--blush);}
  .decor--middle{width:212px;background:
    radial-gradient(circle at 22% 22%,var(--coral) 0%,var(--peach) 18%,rgba(247,201,179,0) 28%),
    radial-gradient(circle at 78% 22%,var(--coral) 0%,var(--peach) 18%,rgba(247,201,179,0) 28%),
    linear-gradient(180deg,var(--blush) 0%,var(--blush) 38%,var(--orange) 55%,var(--wine) 85%,var(--orange) 100%);}
  .decor--right{width:110px;background:
    radial-gradient(ellipse 70% 45% at 65% 52%,var(--orange) 0%,var(--orange) 55%,rgba(232,80,42,0) 75%),
    radial-gradient(ellipse 60% 30% at 55% 82%,var(--coral) 0%,rgba(240,138,106,0) 80%),
    var(--blush);}
  .panel{background:var(--cream);height:100%;position:relative;box-sizing:border-box;}
  .panel--front{width:138px;text-align:center;padding-top:12px;}
  .panel--back{width:134px;text-align:center;padding:12px 8px 0;}
  .brand{display:flex;align-items:center;justify-content:center;gap:5px;height:36px;}
  .brand__dot{width:10px;height:10px;border-radius:50%;background:var(--teal);}
  .brand__name{font-weight:600;font-size:12px;color:var(--teal);}
  .title{font-family:"Caveat Brush",cursive;font-weight:400;color:var(--orange);font-size:30px;line-height:27px;margin:14px 0 0;}
  .cocoa{width:50px;height:24px;margin:6px auto 0;border-radius:50%;background:linear-gradient(90deg,#5c8a3a,#7a4a2e 45%,#5a3220);}
  .claim{font-family:"Caveat Brush",cursive;color:var(--tan);font-size:14px;line-height:16px;margin-top:10px;white-space:nowrap;}
  .ar{font-family:"Cairo",sans-serif;direction:rtl;}
  .claim-ar{color:var(--orange);font-size:8px;line-height:10px;font-weight:700;margin-top:1px;}
  .badge-skin{
    margin:8px auto 0;width:92px;padding:3px 0 3px;background:var(--orange);border-radius:10px;
    color:#fff;font-weight:700;font-size:12px;line-height:11px;box-shadow:0 0 0 2px var(--cream),0 0 0 3px var(--orange);
  }
  .badge-skin .ar{font-size:9px;line-height:11px;}
  .free{font-size:6.5px;color:var(--tan);margin-top:8px;font-weight:600;}
  .weight{font-size:9px;font-weight:700;color:var(--orange);margin-top:2px;}
  .weight__e{font-size:15px;vertical-align:-2px;margin-right:3px;}
  .vegan{
    position:absolute;left:110px;top:100px;width:50px;height:50px;border-radius:50%;background:var(--tan);
    color:#fff;font-size:11px;font-weight:700;line-height:11px;display:flex;flex-direction:column;align-items:center;justify-content:center;z-index:2;
  }
  .vegan small{font-size:5.5px;line-height:6px;}
  .back-text{font-size:5.6px;line-height:7px;color:var(--ink);margin-top:48px;}
  .back-text p{margin:0 0 8px;}
  .back-text .ar{display:block;color:var(--orange);font-size:5.5px;line-height:7px;margin-top:3px;}
  .company{color:var(--orange);font-weight:700;font-size:6px;margin-top:10px;}
  .address{font-size:5px;line-height:7px;}
  .fields{margin-top:9px;text-align:left;font-size:5px;}
  .field{display:flex;align-items:center;gap:3px;margin-bottom:4px;}
  .field__box{width:52px;height:7px;border:0.5px solid var(--ink);border-radius:4px;}
  .field__box--short{width:48px;}
  .pao{font-size:5px;border:0.5px solid var(--ink);padding:0 2px;margin-left:6px;}
</style>
</head>
<body>
  <div class="label">
    <div class="decor decor--left" role="img" aria-label="Illustration: feuilles et gousses de cacao stylisées en tons corail et pêche"></div>

    <section class="panel panel--front">
      <div class="brand"><span class="brand__dot"></span><span class="brand__name">Solenne</span></div>
      <h1 class="title">Déodorant<br>solide</h1>
      <div class="cocoa" role="img" aria-label="Illustration d'une cabosse de cacao avec feuilles"></div>
      <div class="claim">Au beurre de cacao</div>
      <div class="ar claim-ar">مزيل العرق الصلب<br>مع زبدة الكاكاو</div>
      <div class="badge-skin">peau<br>sensible<div class="ar">البشرة الحساسة</div></div>
      <div class="free">Sans aluminium - Sans alcool- Bio</div>
      <div class="weight"><span class="weight__e">e</span>40g</div>
      <div class="vegan">100%<small>naturlich &amp;<br>vegan</small></div>
    </section>

    <div class="decor decor--middle" role="img" aria-label="Illustration: fleurs de cacao et feuillage stylisés, corail, rouge et bordeaux"></div>

    <section class="panel panel--back">
      <div class="brand"><span class="brand__dot"></span><span class="brand__name">Solenne</span></div>
      <div class="back-text">
        <p>Application: poussez le stick d'en bas et appliquez le déodorant sous l'aisselle. Ne pas utiliser sur une peau irritée ou blessée.
          <span class="ar">ادفع العصا من الأسفل وضع مزيل العرق تحت الإبط<br>لا يستخدم على البشرة المتهيجة أو المصابة</span></p>
        <p>Ingrédients: beurre de cacao, amidon de maïs, huile de coco, oxyde de zinc, cire d'abeille
          <span class="ar">المكونات: زبدة الكاكاو، نشا الذرة، زيت جوز الهند، أكسيد الزنك، شمع العسل</span></p>
        <div class="company">Solenne Atelier</div>
        <div class="address">12 Rue des Jasmins 31000 Oran<br>contact@solenne-atelier.com</div>
        <div class="fields">
          <div class="field">Date de Fabrication: <span class="field__box"></span></div>
          <div class="field">Lot: <span class="field__box field__box--short"></span><span class="pao">6M</span></div>
        </div>
      </div>
    </section>

    <div class="decor decor--right" role="img" aria-label="Illustration: feuilles et gousses de cacao stylisées en tons corail et pêche"></div>
  </div>
</body>
</html>
```